Website Landing Page for Brightfall Systems

Create a custom designed website landing page for our business. Looking for a professional upscale design that incorporates our logo and logo colors into the theme. I want a standard fixed frame website, not a constant scrolling format that seems to be the trend. To start with I'm looking for more of the graphic design part, maybe a concept or theme, I don't expect to see a finished project. Not interested in generic templates or layouts.

The name of our company is Brightfall Systems and I've attached our logo below. I'd like to have the web page have the same look and feel of our logo, as well as the colors. Our company, Brightfall Systems does system design, installation, and programming, of residential and commercial Audio/Video and Automation systems. We do home theaters, lighting and building automation, video conferencing systems, security camera installations, conference rooms, projectors, distributed audio systems, and similar Technology projects. This will be a professional services/informational website. We will not sell products on this website. This website will be used to advertise our company and communicate our services to prospective customers. Having a well designed, professional and clean website is one way we want to distinguish our company from the competition.

Here are some examples of what I consider a professional well designed website
http://www.qorlamstudio.com/Work/

Last year we had our tradlo store designed (with PixelMarket) and I'm really happy with the way it turned out. You can see it at www.HolvenGearDepot.com I consider this to be a great design and looking for the same level of quality with this new website. However, do not copy or use any part of this design in this new project. This tradlo store is completely separate from our other company Brightfall Systems. I only mention this tradlo store an an example of good work.

Reason: Still going through designs.

Reason: Still working on project and have not had time to review all designs and request revisions.

Reason: Sill going through designs and requesting revisions

Reason: still going through all the submissions we received.

Target Market(s)

People interested in Audio/Video, home theaters, home automation. We do sales, system design, and programming. We typically work on larger projects with both residential and commercial customers.

Industry/Entity Type

Business

Number of Pages Required

1 page

Requirements
Must have
• Great design elements. Please use a white background. I think white goes well with our logo colors.

```html
<!DOCTYPE html>
<html lang="en">
<head>
<meta charset="utf-8">
<title>Brightfall Systems</title>
<link href="https://fonts.googleapis.com/css2?family=Montserrat:wght@400;500;600&family=Roboto:wght@300;400&family=Open+Sans:wght@400&display=swap" rel="stylesheet">
<style>
  :root {
    --page-bg: #f2f2f2;
    --brand-green: #5db81f;
    --brand-blue: #3f88cf;
    --soft-green: #c6e3ad;
    --soft-blue: #c5d8e8;
    --kitchen-grey: #9a9a9c;
    --kitchen-light: #d9d9db;
    --ink: #2b2b2b;
    --white: #ffffff;
  }
  * { box-sizing: border-box; margin: 0; padding: 0; }
  html, body { width: 1200px; height: 1120px; overflow: hidden; background: var(--page-bg); }
  .canvas { position: relative; width: 1200px; height: 1120px; overflow: hidden; background: var(--page-bg); font-family: "Montserrat", sans-serif; }

  .tile { position: absolute; transform: rotate(45deg); border-radius: 34px; }
  .tile-soft-left  { left: -256px; top: 88px;  width: 399px; height: 399px; background: linear-gradient(135deg, #bfe0a3, #cfe8bb); }
  .tile-soft-right { left: 966px;  top: 100px; width: 399px; height: 399px; background: linear-gradient(135deg, #bfe0a3, #d0e8bc); }
  .tile-hero       { left: 200px;  top: 248px; width: 399px; height: 399px; background: var(--brand-green); }
  .tile-mist-top   { left: 601px;  top: 180px; width: 203px; height: 203px; border-radius: 22px; background: linear-gradient(135deg, #b9cfe2, #d2e1ee); }
  .tile-mist-low   { left: 385px;  top: 727px; width: 203px; height: 203px; border-radius: 22px; background: linear-gradient(135deg, #bdd1e3, #cfdeeb); }
  .tile-kitchen-lg { left: 610px;  top: 425px; width: 489px; height: 489px; border-radius: 40px; background: linear-gradient(180deg, #e8e8ea 0%, #b9b4b2 45%, #6b5b57 60%, #8e8e90 75%, #a9a9ab 100%); }
  .tile-kitchen-sm { left: -108px; top: 554px; width: 399px; height: 399px; background: linear-gradient(180deg, #dcdcde 0%, #a9abad 45%, #3a3a3c 62%, #cfcfd1 80%, #b7b3ac 100%); }

  .site-header { position: absolute; inset: 0 0 auto 0; height: 120px; }
  .brand { position: absolute; left: 234px; top: 34px; display: flex; align-items: center; gap: 17px; }
  .brand-mark { width: 72px; height: 72px; border-radius: 50%; border: 6px solid var(--brand-blue); }
  .brand-name { font-family: "Montserrat", sans-serif; font-weight: 600; font-size: 21px; line-height: 23px; letter-spacing: 1px; text-transform: uppercase; color: var(--brand-blue); }

  .account { position: absolute; top: 20px; left: 704px; display: flex; gap: 12px; }
  .btn { display: flex; align-items: center; justify-content: center; width: 125px; height: 34px; border-radius: 17px; font-size: 9px; font-weight: 600; text-decoration: none; }
  .btn-login { border: 2px solid var(--brand-green); color: var(--brand-green); }
  .btn-register { background: var(--brand-blue); color: var(--white); }

  .main-nav { position: absolute; top: 76px; left: 548px; display: flex; gap: 0; font-size: 12px; color: var(--ink); }
  .main-nav a { color: var(--ink); text-decoration: none; position: absolute; white-space: nowrap; }
  .cart { position: absolute; left: 937px; top: 72px; width: 28px; height: 24px; }

  .hero-copy { position: absolute; left: 190px; top: 350px; width: 420px; text-align: center; color: var(--white); }
  .hero-kicker { font-size: 28px; font-weight: 500; line-height: 34px; }
  .hero-title { font-size: 36px; font-weight: 500; line-height: 44px; margin-top: 2px; }
  .hero-text { font-family: "Roboto", sans-serif; font-weight: 300; font-size: 10.2px; line-height: 17.6px; width: 340px; margin: 10px auto 0; }
  .btn-more { display: inline-flex; align-items: center; justify-content: center; margin-top: 16px; width: 125px; height: 34px; border-radius: 17px; background: var(--white); color: var(--brand-green); font-size: 11px; font-weight: 500; text-decoration: none; }

  .site-footer { position: absolute; top: 1018px; left: 0; width: 970px; text-align: center; font-family: "Open Sans", sans-serif; font-size: 10px; color: var(--ink); }
</style>
</head>
<body>
<div class="canvas">
  <div class="tile tile-soft-left" role="img" aria-label="Faded green-tinted kitchen photograph"></div>
  <div class="tile tile-soft-right" role="img" aria-label="Faded green-tinted kitchen photograph"></div>
  <div class="tile tile-mist-top" role="img" aria-label="Faded blue-tinted photo of a kitchen range hood"></div>
  <div class="tile tile-kitchen-lg" role="img" aria-label="Photo of a modern kitchen with window, potted plants and a toaster on the counter"></div>
  <div class="tile tile-kitchen-sm" role="img" aria-label="Photo of a bright white kitchen with dark countertops"></div>
  <div class="tile tile-mist-low" role="img" aria-label="Faded blue-tinted photo of potted plants on a windowsill"></div>
  <div class="tile tile-hero"></div>

  <header class="site-header">
    <div class="brand">
      <span class="brand-mark"></span>
      <span class="brand-name">Brightfall<br>Systems</span>
    </div>
    <div class="account">
      <a class="btn btn-login" href="#">Log in</a>
      <a class="btn btn-register" href="#">Register</a>
    </div>
    <nav class="main-nav">
      <a href="#" style="left:0">Home</a>
      <a href="#" style="left:65px">About Us</a>
      <a href="#" style="left:147px">Services</a>
      <a href="#" style="left:222px">Products</a>
      <a href="#" style="left:302px">Contact Us</a>
    </nav>
    <svg class="cart" viewBox="0 0 28 24" aria-label="Cart, 2 items">
      <path d="M1 4h4l3 11h12l3-8H7" fill="none" stroke="#3f88cf" stroke-width="2" stroke-linejoin="round"/>
      <path d="M8 9.5h14M9 12.5h12" stroke="#3f88cf" stroke-width="1.2"/>
      <circle cx="10" cy="19" r="1.8" fill="#3f88cf"/>
      <circle cx="19" cy="19" r="1.8" fill="#3f88cf"/>
      <circle cx="22" cy="5" r="5" fill="#3f88cf"/>
      <text x="22" y="7.2" text-anchor="middle" font-size="6" font-family="Montserrat, sans-serif" fill="#fff">2</text>
    </svg>
  </header>

  <section class="hero-copy">
    <p class="hero-kicker">Welcome to</p>
    <h1 class="hero-title">Brightfall Systems</h1>
    <p class="hero-text">Lorem Ipsum is simply dummy text of the printing and typesetting industry. Lorem Ipsum has been the industry's standard dummy text ever since the 1500s, when an unknown printer took a galley of type and scrambled it to make a type specimen book.</p>
    <a class="btn-more" href="#">Read More</a>
  </section>

  <footer class="site-footer">Copyright © 2017 . Brightfall Systems . All Rights Reserved</footer>
</div>
</body>
</html>
```